We are needing a bookcover for a reprint of our book "Whispers Beneath the Cobalt Ridgelands". It takes a look at the geologic formation found in the great plains. Our original cover was colorful and showed rock layers. Something similar but different and eye catching would be great. a geologic cross section showing various layers or possibly some different rocks/soils. We are really open to suggestions attached is the current book cover with the colored layers and the cover from the 80s.

Target Market(s)

Adult Readers

Industry/Entity Type

Nonprofit retail - science - nature

Requirements
Must have
• Geology or rock layers
Nice to have
• Books title, Geologic cross section
Should not have
• People or animals, no photos prefer sketch

```html
<!DOCTYPE html>
<html lang="en">
<head>
<meta charset="utf-8">
<title>Whispers Beneath the Cobalt Ridgelands — Book Cover</title>
<link href="https://fonts.googleapis.com/css2?family=Bebas+Neue&display=swap" rel="stylesheet">
<style>
  :root {
    --page-bg: #f3f3f1;
    --cover-cream: #f5e2b0;
    --cover-cream-light: #f7e8c4;
    --title-rust: #b04a2b;
    --divider-slate: #5d6a73;
    --sun-orange: #f6a94a;
    --sun-gold: #f8c252;
    --sun-yellow: #f9d466;
    --sky-glow: #fbe9b4;
    --mesa-peach: #f0bd8e;
    --mesa-clay: #e2a074;
    --mesa-rust: #d08a62;
    --strata-tan: #c4a98f;
    --strata-taupe: #a89684;
    --strata-stone: #8c8780;
    --strata-grey: #77746f;
    --strata-ash: #8d8982;
    --strata-slate: #64615d;
    --strata-smoke: #74706a;
    --strata-dark: #555350;
    --strata-deep: #484744;
    --strata-base: #3d3c3a;
  }
  * { margin: 0; padding: 0; box-sizing: border-box; }
  html, body {
    width: 1200px;
    height: 2386px;
    overflow: hidden;
    background: var(--page-bg);
  }
  .book-cover {
    position: absolute;
    left: 0;
    top: 295px;
    width: 1200px;
    height: 1796px;
    background: linear-gradient(180deg, var(--cover-cream) 0%, var(--cover-cream-light) 40%, var(--cover-cream) 100%);
    overflow: hidden;
  }
  .title {
    position: absolute;
    left: 0;
    width: 100%;
    text-align: center;
    font-family: "Bebas Neue", "Oswald", sans-serif;
    font-weight: 400;
    color: var(--title-rust);
    line-height: 1;
    white-space: nowrap;
  }
  .title-line-one { top: 92px; font-size: 168px; }
  .title-line-two { top: 356px; font-size: 160px; }
  .title-joiner {
    position: absolute;
    left: 0;
    top: 262px;
    width: 100%;
    height: 100px;
  }
  .title-joiner svg {
    position: absolute;
    left: 0;
    top: 0;
  }
  .title-joiner-word {
    position: absolute;
    left: 0;
    top: 8px;
    width: 100%;
    text-align: center;
    font-family: "Bebas Neue", "Oswald", sans-serif;
    font-size: 100px;
    line-height: 1;
    color: var(--divider-slate);
  }
  .landscape-illustration {
    position: absolute;
    left: 0;
    top: 560px;
    width: 1200px;
    height: 1236px;
    background:
      linear-gradient(180deg,
        transparent 0px, transparent 479px,
        var(--mesa-peach) 479px, var(--mesa-peach) 500px,
        var(--mesa-clay) 500px, var(--mesa-clay) 520px,
        var(--mesa-peach) 520px, var(--mesa-peach) 548px,
        var(--mesa-rust) 548px, var(--mesa-rust) 580px,
        var(--strata-tan) 580px, var(--strata-tan) 622px,
        var(--strata-taupe) 622px, var(--strata-taupe) 670px,
        var(--strata-stone) 670px, var(--strata-stone) 722px,
        var(--strata-grey) 722px, var(--strata-grey) 790px,
        var(--strata-ash) 790px, var(--strata-ash) 850px,
        var(--strata-slate) 850px, var(--strata-slate) 930px,
        var(--strata-smoke) 930px, var(--strata-smoke) 1000px,
        var(--strata-dark) 1000px, var(--strata-dark) 1080px,
        var(--strata-deep) 1080px, var(--strata-deep) 1160px,
        var(--strata-base) 1160px, var(--strata-base) 1236px),
      radial-gradient(circle 273px at 600px 306px,
        var(--sun-orange) 0%, var(--sun-gold) 55%, var(--sun-yellow) 99%, transparent 100%),
      radial-gradient(circle 460px at 600px 330px,
        var(--sky-glow) 0%, rgba(251, 233, 180, 0) 100%);
  }
</style>
</head>
<body>
  <main class="book-cover">
    <h1 class="title title-line-one">Whispers Beneath</h1>
    <div class="title-joiner">
      <svg width="1200" height="100" viewBox="0 0 1200 100" aria-hidden="true">
        <polygon points="103,50 530,41 530,59" fill="var(--divider-slate)"/>
        <polygon points="670,41 1097,50 670,59" fill="var(--divider-slate)"/>
      </svg>
      <span class="title-joiner-word">The</span>
    </div>
    <h1 class="title title-line-two">Cobalt Ridgelands</h1>
    <div class="landscape-illustration" role="img" aria-label="Sketched badlands at sunset: a large golden sun over distant layered mesas, with grey stacks of horizontally bedded sandstone rock layers, sagebrush and a winding dirt trail in the foreground"></div>
  </main>
</body>
</html>
```